Brand new letterhead, business card, email signature etc.

We are a financial company in London, UK. Our website is www.quorvane.com. We're wanting a complete remodel of the company colours, letter head, business cards, email signatures, etc. Looking to keep the same font for the company name. I have upload a colour palette that we want to work with. We're looking for company letterhead for outgoing letters/ correspondence, letterhead for internal documentation, email signatures, e-letters. etc. Ultimately we will redesign the entire website also. It is important that our clients get a strong, secure, warm, trustworthy, solid feeling and first impression.
Updates

Designs look the same

Target Market(s)

Institutional investors, (ultra) high net worth individuals

Industry/Entity Type

Finance, Invesments banking.

Font styles to use
Other font styles liked:
• Current font is "Champagne & Limousines"

Requirements
Must have
• Must use the colours provided on the PDF uploaded to the portal. The purple = main colour. The red = accent colour.
Nice to have
• Nice to use same font as now for the company name "Marlowin". Font is "Champagne & Limousines". Nice to have some reference to the old logo flower, but only subtle.
Should not have
• Do not use the colour red from our website. Use the colours provided on the colour palette PDF that I uploaded in the portal.

```html
<!DOCTYPE html>
<html lang="en">
<head>
<meta charset="utf-8">
<title>Marlowin Letterhead</title>
<link rel="stylesheet" href="https://fonts.googleapis.com/css2?family=Josefin+Sans:wght@300&family=Quicksand:wght@400&display=swap">
<style>
  :root {
    --backdrop: #eeeae8;
    --paper: #ffffff;
    --brand-purple: #4a2a63;
    --accent-red: #d9381e;
    --rule-grey: #dcd6cf;
    --rule-dark: #2a1f30;
    --brand-ink: #4a2a63;
    --footer-ink: #7d7386;
  }
  * { margin: 0; padding: 0; box-sizing: border-box; }
  html, body {
    width: 1191px;
    height: 1200px;
    overflow: hidden;
    background: var(--backdrop);
  }
  .letterhead {
    position: absolute;
    left: 200px;
    top: 40px;
    width: 792px;
    height: 1120px;
    background: var(--paper);
    box-shadow: 0 10px 30px rgba(0, 0, 0, 0.12);
  }
  .brand {
    position: absolute;
    left: 133px;
    top: 49px;
    display: flex;
    align-items: center;
    gap: 11px;
  }
  .brand-mark {
    width: 53px;
    height: 53px;
    border: 1px solid var(--brand-purple);
  }
  .brand-name {
    font-family: "Josefin Sans", sans-serif;
    font-weight: 300;
    font-size: 31px;
    letter-spacing: 3px;
    color: var(--brand-ink);
    line-height: 1;
    padding-top: 6px;
  }
  .header-rules {
    position: absolute;
    left: 133px;
    top: 117px;
  }
  .footer-rule {
    position: absolute;
    left: 133px;
    top: 977px;
  }
  .footer-text {
    position: absolute;
    left: 0;
    width: 100%;
    top: 994px;
    text-align: center;
    font-family: "Quicksand", sans-serif;
    font-size: 8px;
    line-height: 10px;
    color: var(--footer-ink);
  }
  .footer-web { margin-bottom: 6px; }
</style>
</head>
<body>
  <main class="letterhead">
    <header class="brand">
      <span class="brand-mark"></span>
      <span class="brand-name">MARLOWIN</span>
    </header>

    <svg class="header-rules" width="500" height="22" viewBox="0 0 500 22" aria-hidden="true">
      <line x1="2.5" y1="2.5" x2="489" y2="2.5" stroke="var(--brand-purple)" stroke-width="5" stroke-linecap="round"/>
      <line x1="0" y1="10.5" x2="459" y2="10.5" stroke="var(--rule-grey)" stroke-width="2"/>
      <circle cx="466" cy="10.5" r="1.3" fill="var(--rule-grey)"/>
      <circle cx="475" cy="10.5" r="1.3" fill="var(--rule-grey)"/>
      <line x1="0" y1="16.5" x2="420" y2="16.5" stroke="var(--rule-dark)" stroke-width="2"/>
      <circle cx="424" cy="16.5" r="2" fill="var(--accent-red)"/>
    </svg>

    <svg class="footer-rule" width="500" height="6" viewBox="0 0 500 6" aria-hidden="true">
      <line x1="2.5" y1="2.5" x2="489" y2="2.5" stroke="var(--brand-purple)" stroke-width="5" stroke-linecap="round"/>
    </svg>

    <footer class="footer-text">
      <p class="footer-web">www.quorvane.com</p>
      <p class="footer-address">Marlowin (IOA) Limited Fenwick House Harlow Bay<br>Isle of Arden AR42 7QT</p>
    </footer>
  </main>
</body>
</html>
```